50 Page Catalog Full Redesign New Look

We are looking for a redesign of our Catalog,

We are looking for a modern redesign of our Catalog, with our new logo most of the products will be the same with some new products as well.
Please use colors in the new logo attached
Attached is our current design please see this for what product will go in the catulog
Updates

Designs look the same

Target Market(s)

Automotive

Font styles to use
Other font styles liked:
• Our Font is outfit

Colors

Designer to choose colors to be used in the design.

```html
<!DOCTYPE html>
<html lang="en">
<head>
<meta charset="utf-8">
<title>Kestrel Promotional – 2021 Automotive Catalogue</title>
<link href="https://fonts.googleapis.com/css2?family=Outfit:wght@300;400;500;600;700;800&display=swap" rel="stylesheet">
<style>
:root{
  --bg:#dcdcdc;
  --paper:#ffffff;
  --ink:#1a1a1a;
  --muted:#3a3a3a;
  --blue:#0a6aa8;
  --navy:#0d2e5c;
  --grey-bar:#6f6f6f;
  --eu:#1f3a93;
  --card-shadow:0 4px 18px rgba(0,0,0,.12);
}
*{box-sizing:border-box;margin:0;padding:0}
html,body{width:1200px;height:5236px;overflow:hidden}
body{background:var(--bg);font-family:'Outfit',sans-serif;color:var(--ink);position:relative}
.page{position:absolute;left:203px;width:792px;height:1118px;background:var(--paper);box-shadow:0 2px 8px rgba(0,0,0,.15);overflow:hidden}
.abs{position:absolute}

/* cover */
.cover{top:224px;background:#07090d}
.cover-photo{position:absolute;inset:0;background:radial-gradient(ellipse 60% 30% at 52% 42%,#4a5a78 0%,#1c2638 40%,#090c12 75%,#05070b 100%)}
.cover-year{left:112px;top:860px;font-size:128px;font-weight:700;color:#fff;letter-spacing:-2px;line-height:1}
.cover-sub{left:113px;top:990px;font-size:23px;font-weight:400;color:#fff}
.cover-rule{left:465px;top:854px;width:3px;height:162px;background:#fff}
.brand{display:flex;flex-direction:column;align-items:center;color:#fff}
.cover-brand{left:500px;top:872px;width:190px}
.brand-mark{width:70px;height:70px;border:4px solid #fff;border-radius:50%}
.brand-name{font-size:36px;font-weight:500;letter-spacing:4px;margin-top:10px;line-height:1}
.brand-tag{font-size:13px;font-weight:500;letter-spacing:2px;margin-top:4px}
.cover-credit{right:22px;bottom:14px;font-size:7px;color:#777}

/* section headings */
.sec-head{display:flex;align-items:center;gap:8px;font-weight:700;font-size:24px;color:var(--ink)}
.sec-dot{width:26px;height:22px;position:relative}
.sec-dot::before,.sec-dot::after{content:"";position:absolute;top:2px;width:18px;height:18px;border-radius:50%}
.sec-dot::before{left:0;background:var(--navy)}
.sec-dot::after{left:7px;background:var(--blue)}

/* about page */
.about{top:1444px}
.about-head{left:77px;top:82px}
.about-copy{left:133px;top:134px;width:530px;font-size:16px;line-height:24px;color:var(--muted);font-weight:300}
.value-card{width:292px;height:120px;background:#fff;border-radius:10px;box-shadow:var(--card-shadow);display:flex;align-items:center;gap:16px;padding:0 18px}
.value-card svg{flex:0 0 auto}
.value-title{font-size:17px;font-weight:600;color:var(--ink)}
.value-text{font-size:13.5px;line-height:17px;color:var(--muted);font-weight:300}

/* footers */
.footer{left:0;width:792px;height:30px}
.footer-rule{position:absolute;height:1px;background:var(--ink);top:15px}
.footer-text{position:absolute;top:6px;font-size:14.5px;color:var(--ink)}
.footer-text b{font-weight:600}
.footer-mark{position:absolute;top:2px;width:28px;height:28px;border:2px solid var(--blue);border-radius:50%}
.footer-sep{position:absolute;top:3px;width:2px;height:26px;background:var(--ink)}
.footer-num{position:absolute;top:6px;font-size:14px;font-weight:600}

/* product pages */
.products-a{top:2669px}
.products-b{top:3895px}
.kr-head{font-size:24px}
.prod-bar{position:absolute;left:0;height:22px;color:#fff;font-weight:700;font-size:20px;line-height:22px;padding-left:82px;white-space:nowrap}
.prod-bar.blue{background:var(--blue)}
.prod-bar.grey{background:var(--grey-bar)}
.made-in{position:absolute;display:flex;align-items:center;gap:8px}
.made-in .seal{width:50px;height:50px;border-radius:50%;background:var(--eu)}
.made-in .label{font-size:17px;line-height:15px;color:var(--ink)}
.made-in .label strong{display:block;font-size:21px;font-weight:700;line-height:18px;letter-spacing:-.5px}
.spec{position:absolute;font-size:13px;line-height:24px;color:var(--ink)}
.spec b{font-weight:700}
.spec span{margin-left:10px}

/* product shots: one soft tile per keyring, in the item's main tone */
.shot{position:absolute;border-radius:18px}
.tone-blue{background:radial-gradient(ellipse at 50% 62%,#7aa6d8 0%,#c9d9ec 45%,#fff 75%)}
.tone-teal{background:radial-gradient(ellipse at 50% 62%,#3aa6b8 0%,#bfe0e6 45%,#fff 75%)}
.tone-black{background:radial-gradient(ellipse at 50% 62%,#2a2a2a 0%,#b9b9b9 45%,#fff 75%)}
.tone-orange{background:radial-gradient(ellipse at 50% 62%,#e8742a 0%,#f4c7a6 45%,#fff 75%)}
.tone-sky{background:radial-gradient(ellipse at 50% 62%,#9bc3ea 0%,#dbe8f5 45%,#fff 75%)}
.tone-red{background:radial-gradient(ellipse at 45% 65%,#d81e1e 0%,#f1a9a9 42%,#fff 72%)}
.tone-leather{background:radial-gradient(ellipse at 45% 60%,#3b3b3b 0%,#bdbdbd 45%,#fff 75%)}
.tone-yellow{background:radial-gradient(ellipse at 45% 60%,#d4b22a 0%,#ece0a8 40%,#c9c9c9 60%,#fff 78%)}
.tone-silver{background:radial-gradient(ellipse at 45% 60%,#8f949a 0%,#d8dadd 45%,#fff 75%)}
</style>
</head>
<body>

<!-- Cover -->
<section class="page cover">
  <div class="cover-photo" role="img" aria-label="Close-up photograph of a dark car front with glowing ring headlights"></div>
  <div class="abs cover-year">2021</div>
  <div class="abs cover-sub">Automotive Products &amp; Ideas</div>
  <div class="abs cover-rule"></div>
  <div class="abs brand cover-brand">
    <div class="brand-mark"></div>
    <div class="brand-name">KESTREL</div>
    <div class="brand-tag">— PROMOTIONAL —</div>
  </div>
  <div class="abs cover-credit">Cover photo credit line</div>
</section>

<!-- About -->
<section class="page about">
  <h2 class="abs sec-head about-head"><span class="sec-dot"></span>HOW WE ARE?</h2>
  <div class="abs about-copy">
    <p>For over three decades, Kestrel has provided complete merchandise solutions for an ever increasing number of Australian corporations and businesses.</p>
    <p>During this time, our already vast range has grown exponentially and our systems have become increasingly more streamlined to cope with the sheer volume.</p>
    <p>Our enviable reputation is built on experience, innovation and economies of scale that come with being a major wholesaler in Australia.</p>
    <p>We pride ourselves on our accountability, efficiency, consistency, instant reporting and above all, the ability to see things from your point of view.</p>
    <p>We love to strategise with you to make sure what we supply will achieve the desired outcome. Every day we see companies giving away merchandise aimlessly and our mission is to supply you with a product that will suit your criteria.</p>
  </div>

  <div class="abs value-card" style="left:84px;top:584px">
    <svg width="66" height="66" viewBox="0 0 66 66" fill="none" stroke="var(--blue)" stroke-width="3" stroke-linejoin="round"><path d="M33 40 C10 26 16 8 27 12 C30 13 32 15 33 18 C34 15 36 13 39 12 C50 8 56 26 33 40Z"/><path d="M6 38 L6 56 M60 38 L60 56" stroke="var(--navy)"/></svg>
    <div><div class="value-title">CARE</div><div class="value-text">Others needs above<br>our own will always<br>result in a win-win.</div></div>
  </div>
  <div class="abs value-card" style="left:417px;top:584px">
    <svg width="66" height="66" viewBox="0 0 66 66" fill="none" stroke="var(--navy)" stroke-width="3" stroke-linecap="round" stroke-linejoin="round"><path d="M12 54 L56 10"/><path d="M36 10 L56 10 L56 30"/><path d="M8 44 L16 44 M22 58 L22 50" stroke="var(--blue)"/></svg>
    <div><div class="value-title">SPEED</div><div class="value-text">Efficiency in<br>everything we do.</div></div>
  </div>
  <div class="abs value-card" style="left:84px;top:745px">
    <svg width="66" height="66" viewBox="0 0 66 66" fill="none" stroke-width="3" stroke-linecap="round" stroke-linejoin="round"><circle cx="33" cy="33" r="28" stroke="var(--navy)"/><circle cx="33" cy="33" r="20" stroke="var(--blue)"/><path d="M24 33 L31 40 L43 26" stroke="var(--navy)"/></svg>
    <div><div class="value-title">SATISFACTION</div><div class="value-text">Exceeding<br>expectations<br>every time.</div></div>
  </div>
  <div class="abs value-card" style="left:417px;top:745px">
    <svg width="66" height="66" viewBox="0 0 66 66" fill="none" stroke-width="3" stroke-linecap="round" stroke-linejoin="round"><rect x="8" y="30" width="10" height="26" stroke="var(--blue)"/><path d="M18 32 L28 30 L32 14 C38 14 38 22 36 28 L52 28 C56 28 57 33 54 36 C57 38 56 42 53 43 C55 46 53 50 50 50 C51 54 48 56 45 56 L18 54Z" stroke="var(--navy)"/><path d="M44 6 L44 12 M54 10 L51 15 M34 8 L37 13" stroke="var(--blue)"/></svg>
    <div><div class="value-title">ENJOYMENT</div><div class="value-text">All with an<br>element of fun.</div></div>
  </div>

  <div class="abs footer" style="top:1041px">
    <div class="footer-rule" style="left:0;width:371px"></div>
    <div class="footer-text" style="left:412px">kestrel<b>promo</b>.com.au</div>
    <div class="footer-mark" style="left:652px"></div>
    <div class="footer-sep" style="left:700px"></div>
    <div class="footer-num" style="left:720px">1</div>
  </div>
</section>

<!-- Keyrings page 34 -->
<section class="page products-a">
  <h2 class="abs sec-head kr-head" style="left:46px;top:47px"><span class="sec-dot"></span>KEYRINGS</h2>

  <div class="prod-bar blue" style="top:104px;width:434px">Domed Label Metal Keyring</div>
  <div class="made-in" style="left:474px;top:91px"><span class="seal"></span><span class="label">MADE IN<strong>EUROPE</strong></span></div>
  <div class="spec" style="left:70px;top:143px"><b>Size:</b><span>Various Sizes and Styles Available with 30mm Ring</span><br><b>Branding Options:</b><span>Full Colour Domed Label</span></div>

  <div class="shot tone-blue" style="left:163px;top:212px;width:170px;height:192px" role="img" aria-label="Metal keyring with blue domed label"></div>
  <div class="shot tone-teal" style="left:330px;top:212px;width:180px;height:192px" role="img" aria-label="Metal keyring with teal domed label"></div>
  <div class="shot tone-black" style="left:505px;top:212px;width:185px;height:192px" role="img" aria-label="Black metal keyring with colourful domed label"></div>
  <div class="shot tone-orange" style="left:125px;top:415px;width:195px;height:192px" role="img" aria-label="Metal keyring with orange and red domed label"></div>
  <div class="shot tone-orange" style="left:300px;top:415px;width:190px;height:192px" role="img" aria-label="Metal keyring with orange domed label"></div>
  <div class="shot tone-sky" style="left:470px;top:415px;width:200px;height:192px" role="img" aria-label="Metal keyring with light blue domed label"></div>

  <div class="prod-bar grey" style="top:667px;width:489px">Rimless Domed Label Metal Keyring</div>
  <div class="made-in" style="left:566px;top:656px"><span class="seal"></span><span class="label">MADE IN<strong>EUROPE</strong></span></div>
  <div class="spec" style="left:70px;top:705px"><b>Size:</b><span>Various Sizes and Styles Available with 30mm Ring</span><br><b>Branding Options:</b><span>Full Colour Domed Label</span></div>

  <div class="shot tone-red" style="left:150px;top:768px;width:240px;height:215px" role="img" aria-label="Red oval rimless domed label keyring"></div>
  <div class="shot tone-black" style="left:395px;top:768px;width:240px;height:215px" role="img" aria-label="Black rectangular rimless domed label keyring"></div>

  <div class="abs footer" style="top:1043px">
    <div class="footer-num" style="left:58px">34</div>
    <div class="footer-sep" style="left:90px"></div>
    <div class="footer-mark" style="left:108px"></div>
    <div class="footer-text" style="left:183px">1800 555 019</div>
    <div class="footer-text" style="left:326px">sales@<b>kestrelpromo</b>.com.au</div>
    <div class="footer-rule" style="left:529px;width:263px"></div>
  </div>
</section>

<!-- Keyrings page 25 -->
<section class="page products-b">
  <h2 class="abs sec-head kr-head" style="right:46px;top:47px;flex-direction:row-reverse"><span class="sec-dot"></span>KEYRINGS</h2>

  <div class="prod-bar grey" style="top:148px;width:434px">Wide Leather Strap Keyring</div>
  <div class="made-in" style="left:474px;top:132px"><span class="seal"></span><span class="label">MADE IN<strong>EUROPE</strong></span></div>
  <div class="spec" style="left:76px;top:184px"><b>Size:</b><span>Various Sizes and Styles Available with 30mm Ring</span><br><b>Branding Options:</b><span>Full Colour Domed Label &nbsp;-&nbsp; Laser Engraving &nbsp;-&nbsp; Embossing</span></div>

  <div class="shot tone-leather" style="left:72px;top:250px;width:180px;height:280px" role="img" aria-label="Wide black leather strap keyring with round black badge"></div>
  <div class="shot tone-yellow" style="left:214px;top:250px;width:170px;height:280px" role="img" aria-label="Wide leather strap keyring with yellow stitching and yellow badge"></div>
  <div class="shot tone-leather" style="left:346px;top:250px;width:170px;height:280px" role="img" aria-label="Wide black leather strap keyring with silver badge"></div>
  <div class="shot tone-silver" style="left:478px;top:250px;width:175px;height:280px" role="img" aria-label="Wide leather strap keyring with plain silver disc"></div>

  <div class="prod-bar blue" style="top:592px;width:434px">Narrow Leather Strap Keyring</div>
  <div class="made-in" style="left:500px;top:579px"><span class="seal"></span><span class="label">MADE IN<strong>EUROPE</strong></span></div>
  <div class="spec" style="left:76px;top:629px"><b>Size:</b><span>Various Sizes and Styles Available with 30mm Ring</span><br><b>Branding Options:</b><span>Full Colour Domed Label &nbsp;-&nbsp; Laser Engraving &nbsp;-&nbsp; Embossing</span></div>

  <div class="shot tone-leather" style="left:62px;top:700px;width:135px;height:285px" role="img" aria-label="Narrow black leather strap keyring with red stitching"></div>
  <div class="shot tone-leather" style="left:192px;top:700px;width:130px;height:285px" role="img" aria-label="Narrow black leather strap keyring with green stitching"></div>
  <div class="shot tone-silver" style="left:320px;top:700px;width:130px;height:285px" role="img" aria-label="Narrow leather strap keyring with silver plate"></div>
  <div class="shot tone-leather" style="left:448px;top:700px;width:125px;height:285px" role="img" aria-label="Narrow black leather strap keyring with black plate"></div>
  <div class="shot tone-silver" style="left:572px;top:700px;width:130px;height:285px" role="img" aria-label="Narrow leather strap keyring with red stitching and silver plate"></div>

  <div class="abs footer" style="top:1045px">
    <div class="footer-rule" style="left:0;width:371px"></div>
    <div class="footer-text" style="left:412px">kestrel<b>promo</b>.com.au</div>
    <div class="footer-mark" style="left:652px"></div>
    <div class="footer-sep" style="left:700px"></div>
    <div class="footer-num" style="left:718px">25</div>
  </div>
</section>

</body>
</html>
```